Best in class business looking for best in class stationery that accurately reflects the brand image we are trying to build as the brand expands throughout the country. The Varying items should be an eye catching design that makes even the simplest letter or small business card stand out in the crowd.

Target Market(s)

Professionals

Industry/Entity Type

Real Estate

Other font styles liked:
• See atttached logo

Requirements
Must have
• Letterhead
• Business cards
• Envelopes
• Labels for larger mailings
Nice to have
• Folders
• Notebook
Should not have
• Stale design elements

```html
<!DOCTYPE html>
<html lang="en">
<head>
<meta charset="utf-8">
<title>Ridgeline Property Group – Stationery</title>
<link href="https://fonts.googleapis.com/css2?family=Open+Sans:ital,wght@0,400;0,600;0,700;1,600&display=swap" rel="stylesheet">
<style>
  :root {
    --bg: #e6e6e6;
    --paper: #f7f7f7;
    --card: #eeeeee;
    --navy: #22398a;
    --band: #3a5fb3;
    --ink: #3c3c3c;
    --fold: #c9c9c9;
    --white: #ffffff;
  }
  * { box-sizing: border-box; margin: 0; padding: 0; }
  html, body { width: 1200px; height: 800px; overflow: hidden; }
  body {
    background: var(--bg);
    font-family: "Open Sans", Arial, sans-serif;
    color: var(--ink);
    position: relative;
  }

  /* Business cards */
  .card {
    position: absolute;
    top: 100px;
    width: 270px;
    height: 155px;
    background: var(--card);
    overflow: hidden;
  }
  .card--front { left: 500px; }
  .card--back { left: 840px; width: 286px; }

  .holder { position: absolute; left: 26px; top: 66px; }
  .holder__name { font-size: 11.5px; font-weight: 700; color: var(--navy); }
  .holder__title { font-size: 8.5px; font-weight: 600; font-style: italic; color: var(--navy); }

  .contact {
    position: absolute;
    border-left: 2px solid var(--navy);
    padding-left: 14px;
    font-size: 6.4px;
    line-height: 1.45;
    color: var(--ink);
  }
  .card--front .contact { left: 168px; top: 30px; height: 100px; }
  .contact__group { margin-bottom: 8px; }
  .contact__icon { display: block; width: 9px; height: 9px; margin-bottom: 2px; }

  /* Brand name blocks */
  .brand {
    position: absolute;
    display: flex;
    flex-direction: column;
    align-items: center;
    font-weight: 600;
    color: var(--navy);
    letter-spacing: 0.03em;
    text-transform: uppercase;
    white-space: nowrap;
  }
  .brand__mark { background: var(--navy); flex: none; }

  .card--back .brand { left: 102px; width: 180px; top: 32px; font-size: 8.5px; gap: 6px; }
  .card--back .brand__mark { width: 22px; height: 22px; }

  .band-art { position: absolute; left: 0; }
  .card--back .band-art { top: 118px; }

  /* Folder */
  .folder {
    position: absolute;
    left: 45px;
    top: 320px;
    width: 860px;
    height: 440px;
    background: var(--paper);
  }
  .folder__fold {
    position: absolute;
    left: 430px;
    top: 0;
    width: 1px;
    height: 100%;
    background: var(--fold);
  }
  .folder .band-art { bottom: 0; }

  .folder .brand--left { left: 14px; top: 248px; font-size: 11px; gap: 5px; }
  .folder .brand--left .brand__mark { width: 22px; height: 22px; }
  .folder .brand--right { left: 640px; top: 252px; font-size: 13px; gap: 6px; }
  .folder .brand--right .brand__mark { width: 24px; height: 24px; }
  .folder .brand--tab { left: 300px; top: 340px; font-size: 5.5px; color: var(--white); }

  .folder .contact {
    left: 340px;
    top: 264px;
    height: 54px;
    font-size: 4px;
    line-height: 1.35;
    padding-left: 0;
    padding-right: 6px;
    border-left: none;
    border-right: 1px solid var(--navy);
    text-align: right;
  }
  .folder .contact__group { margin-bottom: 3px; }
</style>
</head>
<body>

<section class="card card--front" aria-label="Business card, front">
  <div class="holder">
    <p class="holder__name">Daniel Marsh</p>
    <p class="holder__title">Managing Director</p>
  </div>
  <div class="contact">
    <div class="contact__group">
      <svg class="contact__icon" viewBox="0 0 10 10"><path d="M1 3c0-1.5 8-1.5 8 0v1H7V3H3v1H1z M2.5 5h5l1 3h-7z" fill="var(--navy)"/></svg>
      +65 6240 1100 - 5<br>+65 6240 2200 - 5
    </div>
    <div class="contact__group">
      <svg class="contact__icon" viewBox="0 0 10 10"><rect x="1" y="2.5" width="8" height="5.5" fill="var(--navy)"/><path d="M1 2.5l4 3 4-3" stroke="#eee" stroke-width="0.7" fill="none"/></svg>
      info@ridgelinepg.com<br>sales@ridgelinepg.com
    </div>
    <div class="contact__group">
      <svg class="contact__icon" viewBox="0 0 10 10"><path d="M5 9.5C2.5 6.5 2 5.3 2 4a3 3 0 0 1 6 0c0 1.3-.5 2.5-3 5.5z" fill="var(--navy)"/><circle cx="5" cy="4" r="1.1" fill="#eee"/></svg>
      Harbour Walk, Meridian<br>Centre, Singapore, 2040
    </div>
  </div>
</section>

<section class="card card--back" aria-label="Business card, back">
  <div class="brand">
    <span class="brand__mark"></span>
    <span>Ridgeline Property Group</span>
  </div>
  <svg class="band-art" width="286" height="24" viewBox="0 0 286 24">
    <path d="M0 0H286V4H104Q98 4 95 9L90 18Q87 22 82 22H0z" fill="var(--navy)"/>
  </svg>
</section>

<section class="folder" aria-label="Presentation folder, opened flat">
  <div class="folder__fold"></div>

  <div class="brand brand--left">
    <span class="brand__mark"></span>
    <span>Ridgeline Property Group</span>
  </div>

  <div class="contact">
    <div class="contact__group">+65 6240 1100<br>+65 6240 2200</div>
    <div class="contact__group">info@ridgelinepg.com<br>sales@ridgelinepg.com</div>
    <div class="contact__group">Harbour Walk, Meridian<br>Centre, Singapore, 2040</div>
  </div>

  <svg class="band-art" width="860" height="140" viewBox="0 0 860 140">
    <path d="M0 26H860V33H0z" fill="var(--band)"/>
    <path d="M280 26H430V80H296Q288 80 286 70L278 32z" fill="var(--band)"/>
    <path d="M430 26H560Q570 26 576 32L590 48Q596 56 606 56H860V63H430z" fill="var(--band)"/>
  </svg>

  <div class="brand brand--tab">Ridgeline Property Group</div>

  <div class="brand brand--right">
    <span class="brand__mark"></span>
    <span>Ridgeline Property Group</span>
  </div>
</section>

</body>
</html>
```